Design a double sided business card

We are looking for a clean, eye-catching, and contemporary design that enhances the brand and presents a premium, professional image. Our preference is for a brown card with black gloss detailing and embossed elements; however, we are open to creative input and design suggestions that best achieve a strong visual impact.

Please see the attached existing business card for reference. We use both black and brown colours consistently across our branding.

On sample provided

```html
<!DOCTYPE html>
<html lang="en">
<head>
<meta charset="utf-8">
<title>Halden – Business Card</title>
<link rel="stylesheet" href="https://fonts.googleapis.com/css2?family=Lato:wght@400;700&family=Playfair+Display:wght@400&display=swap">
<style>
  :root {
    --backdrop: #2e2e30;
    --card-sand: #c8b59c;
    --card-black: #242425;
    --ink-black: #1b1b1c;
    --gloss-black: #141415;
    --gloss-edge: #3a3a3c;
    --accent-sand: #c8b59c;
    --text-light: #e9e6e1;
  }
  * { margin: 0; padding: 0; box-sizing: border-box; }
  html, body {
    width: 1200px; height: 799px; overflow: hidden;
    background: var(--backdrop);
  }
  .canvas {
    position: relative; width: 1200px; height: 799px;
    display: flex; align-items: center; justify-content: center; gap: 50px;
  }
  .card {
    position: relative; width: 520px; height: 300px;
    border-radius: 4px; overflow: hidden;
    box-shadow: 0 18px 40px rgba(0,0,0,0.45);
  }
  /* Front side */
  .card--front {
    background: var(--card-sand);
    display: flex; flex-direction: column; align-items: center; justify-content: center; gap: 22px;
  }
  .front-mark {
    width: 74px; height: 74px; background: var(--ink-black);
  }
  .wordmark {
    font-family: "Lato", sans-serif; font-weight: 700;
    letter-spacing: 0.32em; text-transform: uppercase;
  }
  .card--front .wordmark { font-size: 34px; color: var(--ink-black); padding-left: 0.32em; }
  /* Back side */
  .card--back { background: var(--card-black); color: var(--text-light); }
  .card--back .wordmark {
    position: absolute; left: 40px; top: 34px;
    font-size: 24px; color: var(--accent-sand);
  }
  .person { position: absolute; left: 40px; top: 82px; }
  .person__name {
    font-family: "Playfair Display", serif; font-weight: 400;
    font-size: 26px; color: var(--accent-sand); letter-spacing: 0.02em; text-transform: uppercase;
  }
  .person__role {
    font-family: "Lato", sans-serif; font-size: 11px; color: var(--text-light); margin-top: 2px;
  }
  .contact {
    position: absolute; left: 40px; top: 158px; list-style: none;
    font-family: "Lato", sans-serif; font-size: 11.5px; line-height: 1.45;
  }
  .contact li { display: flex; gap: 9px; align-items: flex-start; }
  .contact svg { width: 10px; height: 10px; margin-top: 3px; flex: none; fill: var(--accent-sand); }
  .gloss-square {
    position: absolute; right: -40px; bottom: -40px; width: 230px; height: 230px;
    background: linear-gradient(135deg, var(--gloss-edge) 0%, var(--gloss-black) 45%, var(--gloss-black) 100%);
    box-shadow: inset 0 0 0 1px rgba(255,255,255,0.06);
  }
</style>
</head>
<body>
<main class="canvas">
  <section class="card card--front" aria-label="Card front">
    <div class="front-mark"></div>
    <div class="wordmark">Halden</div>
  </section>

  <section class="card card--back" aria-label="Card back">
    <div class="gloss-square"></div>
    <div class="wordmark">Halden</div>
    <div class="person">
      <div class="person__name">Jon Avery</div>
      <div class="person__role">Director</div>
    </div>
    <ul class="contact">
      <li><svg viewBox="0 0 10 10"><path d="M5 0a3.5 3.5 0 0 0-3.5 3.5C1.5 6 5 10 5 10s3.5-4 3.5-6.5A3.5 3.5 0 0 0 5 0zm0 5a1.5 1.5 0 1 1 0-3 1.5 1.5 0 0 1 0 3z"/></svg><span>The Old Mill Lane<br>Eastbridge EB4 2QT</span></li>
      <li><svg viewBox="0 0 10 10"><path d="M2 0l2 2.5-1 1.2c.7 1.4 1.8 2.5 3.2 3.2l1.2-1L10 8l-1.5 2C4 10 0 6 0 1.5z"/></svg><span>0800 000 4417</span></li>
      <li><svg viewBox="0 0 10 10"><path d="M2.5 0h5v10h-5zM3.3 1v7h3.4V1z"/></svg><span>0700 900 1234</span></li>
      <li><svg viewBox="0 0 10 10"><path d="M0 2h10v6H0zm1 .8v.3l4 2.6 4-2.6v-.3z"/></svg><span>jon@halden.co.uk</span></li>
      <li><svg viewBox="0 0 10 10"><circle cx="5" cy="5" r="5"/></svg><span>halden.co.uk</span></li>
    </ul>
  </section>
</main>
</body>
</html>
```